Vital Years Forward an age management group needs a modern looking website developed asap

Vital Years Forward is an age management group lead by a board certified medical doctor (who also specializes in age management medicine) and a 7th degree black belt jiu-jitsu master. Both have joined forces to create a unique doctor supervised anti-aging medical, nutritional, hormonal, exercise protocol never seen before.
This marriage between medicine and athleticism will create the worlds first complete anti-aging program designed for anyone wishing to remain as healthy and as young for as long as possible.

Our Mission and Vision: "To provide clients cutting edge anti aging programs and protocols designed to "turn-back-the-clock-one-second-at-a-time. Let's all Vital Years Forward..together!"

Vital Years Forward's program consists of 6 unique tiers/platforms each encompassing a specific need.
The 6 tiers are:
1. Apex Vigor: A medical doctor supervised unique and proprietary hormone optimization program and protocol developed by a board certified medical doctor trained by Voralithe ( a world leader in age management medicine) who has practiced age management medicine for the past 7 years
2. Apex Trim: A medical doctor supervised unique and proprietary weight management program and protocol developed by a published medical doctor who's diet book "Brighter Mornings: A Kitchen Reset" was just launched
3.Apex Move: A master athlete supervised training program and protocol, with access to a large proprietary exercise video databank developed by a 7th degree black belt jiu-jitsu master.
4. Apex Plate: A chef driven and supervised home delivered healthy meals. Each meal is made from scratch, and is specifically tailored and targeted according to each patient's specific needs.
5. ApexMegaNutri: A doctor formulated-master athlete approved most complete multi vitamin-mineral-anti-oxidant and supplement pack available on the market today. ApexMegaNutri is: made in the USA, and FDA approved vitamin factory, gluten free, sugar free, and artificial color free.
6. Apex Study: A unique CME approved teaching workshop intended for those physicians who lack expertise in age management but want to become proficient in the art of hormone optimization and age management medicine. The 2-day workshop is held twice monthly on Saturday and Sunday in sunny Florida.

This is our scope and goal.
We want to become the leaders in age management medicine by being the first to unite doctors-athletes-chefs-nutritionist together in an effort to deliver the most advanced most cutting edge programs and protocols so we may all : VITAL YAERS FORWARD!

We already have the logo for Vital years forward.
Please keep in mind the following:
1. Apex vigorous should be in green and black
2. Apex trim should be in purple and black
3. Apex move in orange and black
4. Apx plate in yellow and black
5. ApexMegaNurti in red and black
6. Apex study in gray and black

Target Market(s)

Adults Males and females wishing to remain as healthy and as young for as long as possible
Obese and overweight adults males and females
Athletes males and females
Young obese and overweight males and females
ALL can be from any country!

Industry/Entity Type

Health And Wellness

Coding

Coded - Design and coding required

Number of Pages Required

5+ page

Requirements
Must have
• The front page must have our mission statement as well as the 6 tiers/platforms displayed (Apex Vigor, Apex Trim, Apex Move, Apex Plate, ApexMegaNutri, Apex Study) and each platform when "cliked on" should open up in its own unique page.
• The capability for clients to log on to any of the pages using assigned usernames and passwords.
• The capability of check out (credit cards, paypal) from any of the pages. EX the client may want to buy ApexMegaNutri. He/She would click on the main page then click on ApexMeganutri page and choose to buy the vitamin. Same For the rest: He/she may want to buy the weight loss program (apex trim), or the Hormone program (apex vigor) or the food delivered home (apex Plate) or apex move (access to the exercise video databank) or attend the workshop (buy the teaching program..BUT this will ONLY be accessible if the client is a medical doctor and has a valid medical license).
• Also the client may want to have full access to ALL the 6 tiers, thus on the FRONT page we need a checkout with "full access to tiers"
• Also we need to make sure no videos are downloade but only viewed. we need to have this safety built in.
• Also we nee to be able to keep track of emails and have stats. and any email inquiry must be diverted to my iphone.
Nice to have
• Modern look with pop-ups and graphics and iphone and android capability
Should not have
• nothing explicit

```html
<!DOCTYPE html>
<html lang="en">
<head>
<meta charset="utf-8">
<title>Vital Years Forward</title>
<link href="https://fonts.googleapis.com/css2?family=Roboto:wght@400;500;700&family=Nothing+You+Could+Do&display=swap" rel="stylesheet">
<style>
:root{
  --pale:#eef5fd;
  --blue:#3d8ff0;
  --footer:#5aa0f5;
  --ink:#222;
  --grey:#555;
  --card:#0b0b0b;
  --green:#0b7d12;
  --purple:#7d0a82;
  --orange:#f9a400;
  --yellow:#cccc00;
  --red:#f00000;
  --stone:#7a7a7a;
  --white:#fff;
}
*{box-sizing:border-box;margin:0;padding:0}
html,body{width:671px;height:1200px;overflow:hidden}
body{position:relative;font-family:'Roboto',sans-serif;color:var(--ink);background:var(--white)}
.abs{position:absolute}
.topbar{left:0;top:0;width:671px;height:26px;background:var(--pale);text-align:center}
.brand{font-size:15px;font-weight:700;line-height:26px;color:var(--ink);letter-spacing:.5px}
.hero{left:0;top:26px;width:671px;height:306px;
  background:linear-gradient(180deg,#6d7378 0%,#8a8168 30%,#5a4a34 62%,#2e2418 100%)}
.nav{top:44px;font-size:9.5px;color:var(--white)}
.login{left:538px;top:35px;width:37px;height:19px;background:var(--blue);border-radius:3px;
  color:var(--white);font-size:9.5px;line-height:19px;text-align:center}
.hero-title{left:260px;top:116px;width:320px;text-align:center;font-family:'Nothing You Could Do',cursive;
  font-size:40px;color:var(--white);line-height:1}
.hero-sub{left:260px;top:174px;width:320px;text-align:center;font-size:12px;font-weight:500;color:var(--white)}
.btn{top:206px;height:20px;font-size:5.5px;font-weight:700;color:var(--white);text-align:center;line-height:20px;border-radius:2px}
.btn-buy{left:349px;width:72px;background:var(--blue)}
.btn-surf{left:425px;width:59px;border:1px solid var(--white)}
.wellness{left:0;top:332px;width:671px;height:205px;background:var(--pale)}
.sec-title{width:671px;left:0;text-align:center;font-size:12px;font-weight:700;color:var(--ink)}
.dots{height:0;border-top:1px dotted var(--blue)}
.feature-icon{width:42px;height:46px;background:var(--blue);border-radius:2px}
.feature-icon svg{display:block;margin:11px auto 0}
.feature-head{width:200px;text-align:center;font-size:10px;font-weight:700}
.feature-text{width:200px;text-align:center;font-size:7.2px;line-height:11px;color:var(--grey)}
.tier{width:194px;height:140px;background:var(--card);border-radius:3px;color:var(--white);text-align:center;padding:0 9px}
.tier h3{margin-top:38px;font-size:10px;font-weight:700}
.tier p{margin-top:9px;font-size:7.1px;line-height:11px}
.badge{width:52px;height:52px;border-radius:50%}
.footer{left:0;top:965px;width:671px;height:235px;background:var(--footer);color:var(--white)}
.foot-head{top:996px;font-size:10px;font-weight:700}
.foot-text{font-size:7.2px;line-height:11px}
.thumb{width:26px;height:26px;border-radius:50%;background:#c4c4c4;color:#333;font-size:5px;text-align:center;line-height:26px}
.post-title{font-size:7.2px}
.post-meta{font-size:5.8px;margin-top:4px}
.social{top:1120px;width:8px;height:8px;border-radius:50%;background:var(--white)}
.quote{left:499px;top:1013px;font-size:34px;font-weight:700;color:var(--blue);line-height:1}
.avatar{left:501px;top:1085px;width:44px;height:44px;border-radius:50%;background:#c4c4c4;color:#333;font-size:7px;text-align:center;line-height:44px}
.rule{left:29px;top:1161px;width:613px;border-top:1px solid #3a5d8a}
.copy{left:0;top:1177px;width:671px;text-align:center;font-size:7px}
</style>
</head>
<body>

<header class="abs topbar"><span class="brand">Vital Years Forward</span></header>

<section class="abs hero" role="img" aria-label="Photo of a runner's legs on a hilltop trail at sunset"></section>
<nav>
  <span class="abs nav" style="left:104px">Apex vigorous</span>
  <span class="abs nav" style="left:183px">Apex trim</span>
  <span class="abs nav" style="left:260px">Apex move</span>
  <span class="abs nav" style="left:318px">Apx plate</span>
  <span class="abs nav" style="left:382px">ApexMegaNurti</span>
  <span class="abs nav" style="left:467px">Apex study</span>
  <span class="abs login">Login</span>
</nav>
<h1 class="abs hero-title">Ready to Enjoy?</h1>
<p class="abs hero-sub">Grab This Perfect Team Now!</p>
<span class="abs btn btn-buy">I LIKE IT! PURCHASE</span>
<span class="abs btn btn-surf">GO ON SURFING</span>

<section class="abs wellness"></section>
<h2 class="abs sec-title" style="top:346px">Health And Wellness</h2>
<div class="abs dots" style="left:23px;top:368px;width:627px"></div>

<div class="abs feature-icon" style="left:105px;top:391px"><svg width="22" height="22" viewBox="0 0 22 22" fill="none" stroke="#fff" stroke-width="1.4"><path d="M3 10h4v9H3zM7 10l4-7c2 0 2 2 1.5 4H18c1.2 0 2 1 1.7 2.2l-1.6 7.6c-.2 1-1 1.2-2 1.2H7"/></svg></div>
<div class="abs feature-icon" style="left:314px;top:391px"><svg width="22" height="22" viewBox="0 0 22 22" fill="none" stroke="#fff" stroke-width="1.4"><path d="M11 2c3 3 4 7 3 12H8C7 9 8 5 11 2zM8 11l-3 4 3 1M14 11l3 4-3 1M10 18l1 3 1-3"/><circle cx="11" cy="8" r="1.4"/></svg></div>
<div class="abs feature-icon" style="left:523px;top:391px"><svg width="22" height="22" viewBox="0 0 22 22" fill="none" stroke="#fff" stroke-width="1.4"><path d="M5 2h9l4 4v14H5zM14 2v4h4M8 10h7M8 13h7M8 16h7"/></svg></div>

<h3 class="abs feature-head" style="left:26px;top:441px">Who we are</h3>
<h3 class="abs feature-head" style="left:235px;top:441px">Our Mission</h3>
<h3 class="abs feature-head" style="left:444px;top:441px">Our Vision</h3>
<p class="abs feature-text" style="left:26px;top:464px">Vital Years Forward is an age management group lead by a board certified medical doctor (who also specializes in age management medicine) and a 7th degree black belt jiu-jitsu master</p>
<p class="abs feature-text" style="left:235px;top:464px">To provide clients cutting edge anti aging programs and protocols designed to "turn-back-the-clock-one-second-at-a-time. Let's all Vital Years Forward..together!</p>
<p class="abs feature-text" style="left:444px;top:464px">To provide clients cutting edge anti aging programs and protocols designed to "turn-back-the-clock-one-second-at-a-time. Let's all Vital Years Forward..together!</p>

<h2 class="abs sec-title" style="top:544px">Vital Years Forward's Program Consists</h2>
<div class="abs dots" style="left:30px;top:565px;width:612px"></div>

<article class="abs tier" style="left:29px;top:604px"><h3>Apex vigorous</h3><p>A medical doctor supervised unique and proprietary hormone optimization program and protocol developed by a board certified medical doctor trained by Voralithe ( a world leader in age management medicine) who has practiced age management medicine for the past 7 years</p></article>
<article class="abs tier" style="left:238px;top:604px"><h3>Apex trim</h3><p>A medical doctor supervised unique and proprietary weight management program and protocol developed by a published medical doctor who's diet book "Brighter Mornings: A Kitchen Reset" was just launched</p></article>
<article class="abs tier" style="left:448px;top:604px"><h3>Apex move</h3><p>A master athlete supervised training program and protocol, with access to a large proprietary exercise video databank developed by a 7th degree black belt jiu-jitsu master</p></article>
<article class="abs tier" style="left:29px;top:810px"><h3>Apx plate</h3><p>A chef driven and supervised home delivered healthy meals. Each meal is made from scratch, and is specifically tailored and targeted according to each patient's specific needs</p></article>
<article class="abs tier" style="left:237px;top:810px"><h3>ApexMegaNurti</h3><p>A doctor formulated-master athlete approved most complete multi vitamin-mineral-anti-oxidant and supplement pack available on the market today. ApexMegaNutri is: made in the USA, and FDA approved vitamin factory, gluten free, sugar free, and artificial color free.</p></article>
<article class="abs tier" style="left:444px;top:810px"><h3>Apex study</h3><p>A unique CME approved teaching workshop intended for those physicians who lack expertise in age management but want to become proficient in the art of hormone optimization and age management medicine. The 2-day workshop is held twice monthly on Saturday and Sunday in sunny Florida</p></article>

<div class="abs badge" style="left:100px;top:578px;background:var(--green)" role="img" aria-label="White figure of a person in a wide-armed pose"></div>
<div class="abs badge" style="left:309px;top:578px;background:var(--purple)" role="img" aria-label="White figure of a person stretching"></div>
<div class="abs badge" style="left:519px;top:578px;background:var(--orange)" role="img" aria-label="White figure of a person exercising"></div>
<div class="abs badge" style="left:100px;top:784px;background:var(--yellow)" role="img" aria-label="White figure of a person jumping"></div>
<div class="abs badge" style="left:308px;top:784px;background:var(--red)" role="img" aria-label="White figure of a person in a floor stretch"></div>
<div class="abs badge" style="left:515px;top:784px;background:var(--stone)" role="img" aria-label="White figure of a person seated in a yoga pose"></div>

<footer class="abs footer"></footer>
<h4 class="abs foot-head" style="left:29px">Contact Us</h4>
<h4 class="abs foot-head" style="left:186px">Recent Posts</h4>
<h4 class="abs foot-head" style="left:343px">Latest Twitts</h4>
<h4 class="abs foot-head" style="left:501px">Last Review</h4>

<p class="abs foot-text" style="left:29px;top:1019px;width:150px">Maecenas etos sit amet, consectetur adipiscing elit. Terminal volutpat rutrum metro amet sollicitudin interdum.</p>
<p class="abs foot-text" style="left:29px;top:1052px;color:var(--white)">Phone: +1 (800) 555 01 42</p>
<p class="abs foot-text" style="left:29px;top:1078px;color:var(--white)">Office: 1180 Linden Row, Harbor City</p>
<p class="abs foot-text" style="left:29px;top:1096px;color:var(--white)">Email: hello@vitalyearsforward.com</p>
<span class="abs social" style="left:29px"></span>
<span class="abs social" style="left:43px"></span>
<span class="abs social" style="left:58px"></span>
<span class="abs social" style="left:74px"></span>
<span class="abs social" style="left:89px"></span>

<div class="abs thumb" style="left:186px;top:1021px">50x50</div>
<div class="abs" style="left:221px;top:1020px"><p class="post-title">Business Cards Design Trends</p><p class="post-meta">Dec 02, 2020 / 2 comments</p></div>
<div class="abs thumb" style="left:186px;top:1061px">50x50</div>
<div class="abs" style="left:221px;top:1060px"><p class="post-title">This Maravelous App</p><p class="post-meta">Nov 18, 2020 / 9 comments</p></div>
<div class="abs thumb" style="left:186px;top:1101px">50x50</div>
<div class="abs" style="left:221px;top:1100px"><p class="post-title">Brand Paper Niceties</p><p class="post-meta">Nov 10, 2020 / 0 comments</p></div>

<span class="abs quote">&ldquo;</span>
<p class="abs foot-text" style="left:532px;top:1019px;width:112px">Lorem ipsum dolor sit amet, consectetur adipiscing elit, sed do eiusmod tempor incididunt ut labore et dolore magna aliqua. Ut enim ad minim veniam, quis nostrud exercitation ullamco.</p>
<div class="abs avatar">84x84</div>
<p class="abs" style="left:553px;top:1096px;font-size:9.5px">Nolan Ashby</p>
<p class="abs" style="left:553px;top:1114px;font-size:7.2px">Creative Designer</p>

<div class="abs rule"></div>
<p class="abs copy">Copyright 2020. All Rights Reserved by Vital Years Forward's</p>

</body>
</html>
```